Werbebanner für Textilreinigung
Zielgruppe
Wir sind eine Textilreinigung mit einem großen Spektrum an Leistungen.
Unsere Zielgruppe sind Privat Personen die ihre Textilien zum reinigen zu uns bringen.
Aufgabenstellung
Es sollen 5 Straßenbanner designt werden. Diese werden bei Ortseinfahrten/- ausfahrten, aufgehängt. Das Design soll modern sein und zu unserem Logo passen. Die Herausforderung bei den Straßenbannern ist die Zielgruppe, die Autofahrer. Der Banner wird beim Vorbeifahren für nur 1-2 Sekunden gesehen. Auf jedem Banner soll ein Sonderangebot mit eingebaut werden. Zu der Zeit in der der Banner aufgehängt ist, erhält der Kunde 20% auf die jeweilige Dienstleistung.
Hier die verschiedenen Banner:
-Betten & Daunenreinigung | -Trachten und Lederreinigung | -Braut & Festtagskleider reinigung |-Teppichwäsche (inkl. kostenlosen Abhol und Lieferservice) |-Hemdenservice
Bannergröße beträgt 100cm(H) x 300cm(B)
Das gilt für alle 5 verschiedenen Banner.
Es soll auf jedem Banner stehen:
-Sonderangebot 20%
-unser Logo (siehe Dateien)
-unsere Adresse
-Telefonnummer
-Aufruf zur Aktion
Anmerkung: Auf der EPS.Datei muss ein kleiner Schriftzug hinzugefügt werden der auf der PDF. zu sehen ist.

```html
<!DOCTYPE html>
<html lang="de">
<head>
<meta charset="utf-8">
<title>Kissenschlacht – Straßenbanner</title>
<link rel="stylesheet" href="https://fonts.googleapis.com/css2?family=Roboto:wght@300;400;500;700&display=swap">
<style>
  :root {
    --navy: #123f95;
    --green: #5fb12f;
    --white: #ffffff;
    --photo-light: #f3f1ee;
    --photo-shadow: #d9d6d2;
  }
  * { margin: 0; padding: 0; box-sizing: border-box; }
  html, body { width: 1200px; height: 400px; overflow: hidden; background: var(--white); }
  .banner {
    position: relative;
    width: 1200px;
    height: 400px;
    overflow: hidden;
    background: var(--white);
    font-family: "Roboto", Arial, sans-serif;
  }
  .photo {
    position: absolute;
    left: 560px; top: 0;
    width: 640px; height: 400px;
    background:
      radial-gradient(ellipse 180px 160px at 310px 90px, rgba(205,160,110,0.55), transparent 70%),
      radial-gradient(ellipse 150px 190px at 500px 180px, rgba(231,211,176,0.9), transparent 72%),
      linear-gradient(90deg, var(--white) 0%, var(--photo-light) 22%, var(--photo-shadow) 60%, var(--photo-light) 100%);
  }
  .offer-plus {
    position: absolute;
    left: 43px; top: 65px;
    width: 54px; height: 54px;
    background: var(--navy);
    border-radius: 3px;
    z-index: 2;
  }
  .offer-plus svg { display: block; }
  .offer-badge {
    position: absolute;
    left: 70px; top: 89px;
    width: 174px; height: 174px;
    background: var(--green);
    border-radius: 8px;
    color: var(--white);
  }
  .offer-value {
    position: absolute;
    left: 8px; top: 30px;
    font-weight: 500;
    font-size: 88px;
    line-height: 1;
    letter-spacing: -3px;
  }
  .offer-label {
    position: absolute;
    font-weight: 300;
    font-size: 29px;
    line-height: 1;
  }
  .offer-label--first { left: 10px; top: 110px; }
  .offer-label--second { right: 11px; top: 135px; }
  .headline-box {
    position: absolute;
    left: 258px; top: 90px;
    width: 491px; height: 173px;
    background: var(--navy);
    border-radius: 8px;
    color: var(--white);
    font-weight: 700;
    line-height: 1;
    text-transform: uppercase;
    white-space: nowrap;
  }
  .headline-top {
    position: absolute;
    left: 15px; top: 30px;
    font-size: 42px;
    letter-spacing: -0.5px;
  }
  .headline-main {
    position: absolute;
    left: 37px; top: 79px;
    font-size: 74px;
    letter-spacing: -1.5px;
  }
  .brand {
    position: absolute;
    left: 26px; top: 302px;
    color: var(--navy);
  }
  .brand-dot {
    position: absolute;
    left: 0; top: 8px;
    width: 66px; height: 66px;
    border-radius: 50%;
    background: var(--green);
  }
  .brand-services {
    position: absolute;
    left: 103px; top: 2px;
    font-size: 13px;
    font-weight: 500;
    line-height: 16px;
    text-transform: uppercase;
    white-space: nowrap;
  }
  .brand-name {
    position: absolute;
    left: 102px; top: 38px;
    font-size: 32px;
    font-weight: 700;
    letter-spacing: -0.5px;
    line-height: 1;
    white-space: nowrap;
  }
  .brand-motto {
    position: absolute;
    left: 326px; top: 38px;
    font-size: 14px;
    font-weight: 400;
    line-height: 16px;
    white-space: nowrap;
  }
  .brand-motto span { display: block; padding-left: 16px; }
  .contact-box {
    position: absolute;
    left: 951px; top: 297px;
    width: 221px; height: 75px;
    background: var(--green);
    border-radius: 7px;
    color: var(--white);
    font-size: 17px;
    font-weight: 400;
    line-height: 21.5px;
    padding: 5px 0 0 20px;
    text-transform: uppercase;
    white-space: nowrap;
  }
</style>
</head>
<body>
  <div class="banner">
    <div class="photo" role="img" aria-label="Foto: schlafender Hund mit Teddybär auf weißen Kissen und Bettdecke"></div>

    <div class="offer-badge">
      <div class="offer-value">20%</div>
      <div class="offer-label offer-label--first">Aktions</div>
      <div class="offer-label offer-label--second">Rabbat</div>
    </div>
    <div class="offer-plus">
      <svg width="54" height="54" viewBox="0 0 54 54" aria-hidden="true">
        <path d="M27 11 V43 M11 27 H43" stroke="#ffffff" stroke-width="4"/>
      </svg>
    </div>

    <div class="headline-box">
      <div class="headline-top">Kissenschlacht</div>
      <div class="headline-main">Alles klar!</div>
    </div>

    <div class="brand">
      <div class="brand-dot"></div>
      <div class="brand-services">Zentralreinigung<br>Großwäscherei</div>
      <div class="brand-name">GLANZWERK</div>
      <div class="brand-motto">Wir lieben<span>unsere Arbeit</span></div>
    </div>

    <div class="contact-box">
      Lindenweg 7<br>
      86999 Talheim,<br>
      Tel.: 01234 - 5678
    </div>
  </div>
</body>
</html>
```